Kestrel Ridge Partners LLC
Business card and stationary set for Investment Firm - Financial Services
Business card and stationary set for Investment Firm
Simple
Owen Talcott
President / Founder
4820 Birchwood Lane Sparta, IL 62286
owen@talcottwealth.example
www.talcottwealth.example
jdalvin jdalvin
Also, please keep a simple, prestigious / exclusive look to the design.
Designers- I am looking for a design that uses watermarks and different parts of the logo separated out to create some originality. I only want to see the the "Professional Investment Management" one time in the design with the logo. Also, there are 2 formats of the logo in the files I uploaded. One has the graphic on the side and the other on the top. I'd like to see the use of both of these. I do like the blue on the back of the card...maybe a watermark included. The most creative will probably get the win on this. Thank you.
bluequill bluequill
Can u do some sort of star rating, which help us to make these changes,and then i will submit you stationary package with your requirements.. thanks
Also, thank you cards.
Designers - A few things I'll need in the design will be the removal of "Professional Investment Management" from the logo on the front of the card. I still like it to be on the back OR on the larger logo. I only wanted it listed on one of the logos as opposed to both of them. Also, I do like the look and feel of an exclusive, simple, unique design. I do like the back side of the card to be the blue color. I like a background image of the logo as well to add texture. Finally, I need a full stationary design including letterhead, envelopes and return of all sizes (standard and 10X 13), business cards, folders and 1/4 page paper pad. Thank you.
Vandal Vandal
Star Rating please....
Also, please include simple envelope design
Be sure to include standard stationary design as well. The font does not need to be the same as the logo on all pieces.
Designers - Feel free to remove the tagline "Professional Investment Management" in parts of the stationary and business cards. It can be included but isn't necessary. Thank you.

```html
<!DOCTYPE html>
<html lang="en">
<head>
<meta charset="utf-8">
<title>Kestrel Ridge Partners LLC – Business Card</title>
<link rel="stylesheet" href="https://fonts.googleapis.com/css2?family=Cinzel:wght@500&family=Open+Sans:wght@400;600&display=swap">
<style>
  :root {
    --bg: #e9eaeb;
    --card: #ffffff;
    --navy: #1e3f57;
    --teal: #1f6e84;
    --teal-dark: #17566a;
    --silver: #c9ced2;
    --grey: #7d858b;
    --ink: #2c3338;
  }
  * { margin: 0; padding: 0; box-sizing: border-box; }
  html, body { width: 1200px; height: 908px; overflow: hidden; }
  body {
    background: var(--bg);
    font-family: "Open Sans", Arial, sans-serif;
    position: relative;
  }
  .card {
    position: absolute;
    top: 305px;
    width: 520px;
    height: 298px;
    background: var(--card);
    border-radius: 16px;
    overflow: hidden;
    box-shadow: 0 6px 18px rgba(0,0,0,0.12);
  }
  .card--front { left: 50px; }
  .card--back { left: 630px; }

  .brand { display: flex; align-items: center; gap: 10px; }
  .brand__mark { width: 22px; height: 22px; background: var(--navy); }
  .brand__name {
    font-family: "Cinzel", Georgia, serif;
    font-weight: 500;
    color: var(--navy);
    letter-spacing: 0.5px;
  }

  .card--front .brand {
    position: absolute; top: 108px; left: 0; right: 0; justify-content: center;
  }
  .card--front .brand__name { font-size: 24px; }
  .tagline {
    position: absolute; top: 148px; left: 0; right: 0; text-align: center;
    font-size: 8.5px; letter-spacing: 2.4px; color: var(--grey); text-transform: uppercase;
  }
  .tagline::before, .tagline::after {
    content: ""; display: inline-block; width: 34px; height: 1px;
    background: var(--silver); vertical-align: middle; margin: 0 8px;
  }
  .website {
    position: absolute; top: 196px; left: 0; right: 0; text-align: center;
    font-size: 14px; color: var(--grey); letter-spacing: 0.4px;
  }

  .card--back .swoosh { position: absolute; left: 0; bottom: 0; }
  .card--back .brand { position: absolute; top: 40px; right: 40px; }
  .card--back .brand__name { font-size: 17px; }
  .person {
    position: absolute; top: 88px; right: 40px; text-align: right;
  }
  .person__name { font-size: 16px; font-weight: 600; color: var(--navy); }
  .person__title { font-size: 11px; color: var(--grey); margin-top: 2px; }
  .contact {
    position: absolute; top: 132px; left: 150px;
    font-size: 11px; color: var(--ink); line-height: 17px;
    list-style: none;
  }
  .contact li { display: flex; align-items: center; gap: 7px; }
  .contact svg { width: 11px; height: 11px; flex: none; fill: var(--teal); }
  .contact .address { display: block; padding-left: 18px; }
</style>
</head>
<body>

<section class="card card--front">
  <div class="brand">
    <span class="brand__mark"></span>
    <span class="brand__name">Kestrel Ridge Partners LLC</span>
  </div>
  <p class="tagline">Professional Investment Management</p>
  <p class="website">www.talcottwealth.example</p>
</section>

<section class="card card--back">
  <svg class="swoosh" width="520" height="298" viewBox="0 0 520 298" aria-hidden="true">
    <path d="M0 60 C 70 120, 120 220, 150 298 L0 298 Z" fill="var(--silver)"/>
    <path d="M0 74 C 62 130, 106 224, 132 298 L0 298 Z" fill="var(--teal)"/>
    <path d="M0 150 C 40 190, 70 250, 84 298 L0 298 Z" fill="var(--teal-dark)" opacity="0.5"/>
  </svg>

  <div class="brand">
    <span class="brand__mark"></span>
    <span class="brand__name">Kestrel Ridge Partners LLC</span>
  </div>
  <div class="person">
    <p class="person__name">Owen Talcott</p>
    <p class="person__title">President / Founder</p>
  </div>

  <ul class="contact">
    <li class="address">4820 Birchwood Lane<br>Sparta, IL 62286</li>
    <li>
      <svg viewBox="0 0 24 24"><path d="M6.6 10.8a15 15 0 0 0 6.6 6.6l2.2-2.2c.3-.3.7-.4 1-.2 1.1.4 2.3.6 3.6.6.6 0 1 .4 1 1V20c0 .6-.4 1-1 1A17 17 0 0 1 3 4c0-.6.4-1 1-1h3.5c.6 0 1 .4 1 1 0 1.3.2 2.5.6 3.6.1.3 0 .7-.2 1z"/></svg>
      (618) 555-0142
    </li>
    <li>
      <svg viewBox="0 0 24 24"><path d="M2 5h20v14H2z M4 7l8 6 8-6" fill="none" stroke="var(--teal)" stroke-width="2.4"/></svg>
      owen@talcottwealth.example
    </li>
    <li>
      <svg viewBox="0 0 24 24"><circle cx="12" cy="12" r="9" fill="none" stroke="var(--teal)" stroke-width="2.4"/><path d="M3 12h18M12 3c3 3 3 15 0 18M12 3c-3 3-3 15 0 18" fill="none" stroke="var(--teal)" stroke-width="1.8"/></svg>
      www.talcottwealth.example
    </li>
  </ul>
</section>

</body>
</html>
```